WP website design (Pellingworth)

We need a wordpress design for an established auction and real estate company based in Viginia- "The Bid You Trust!". The winning design will incorporate a professional color scheme with company logo in a clean layout. The design needs to consider that this will be developed on a responsive theme.
Industry/Entity Type
Real Estate
Requirements
Must have
- - - We will require winning designer to provide a layered PSD (Adobe photoshop) concept file, along with any non-standard font files used.
- Logo attached. Color scheme should compliment the logo colors; nothing flashy, rather more business oriented … subdued colors. Lighten up the burgundy color; not so dark on the background;
- Horizontal Navigation menu with these pages:
- Home - Upcoming Auctions - Appraisals - Past Auctions - Real Estate for Sale Sellers - Buyers - About Pellingworth - Contact Us
- A slideshow element on the home page use stock of real estate for the initial image.
- Sidebar widgets to be included are: Email sign-up form - Featured Auctions - Testimonial widget - 'Our Videos' widget; Social media icons somewhere in layout (facebook, twitter, RSS, and Youtube, linkedIn), News & Events widget, "Special announcements" blog.
- Homepage content is text:
- Pellingworth is "The bid you trust!"
- Pellingworth Auctioneers International is a premier, full service Auction Company specializing in the sale of commercial and residential real estate through the auction method. In the last 53 years, we have conducted thousands of auctions across the United States and several foreign countries.
- We bring our years of experience in auctioning homes, land, condominiums, industrial properties, retail buildings and development sites to help private individuals, corporations and financial institutions sell their property. In addition, we can assist you with liquidating estates, antiques, equipment and firearms collections.
- We have conducted thousands of auctions, assisting a wide range of companies both large and small achieve maximum value for their capital assets.
Nice to have
- Site will have drop down menus, please show what one will look like.
Should not have
- no gavels should be used in the design

```html
<!DOCTYPE html>
<html lang="en">
<head>
<meta charset="utf-8">
<title>Pellingworth Auctioneers International</title>
<link href="https://fonts.googleapis.com/css2?family=Source+Sans+3:wght@300;400;600&family=Arimo:ital,wght@0,400;0,700;1,400&display=swap" rel="stylesheet">
<style>
:root{
  --navy:#2f4690;
  --blue-band:#3a5296;
  --red:#c8202f;
  --nav-red:#e13b3b;
  --ink:#444;
  --muted:#666;
  --paper:#f1f1f1;
  --white:#fff;
  --footer:#2c2c2c;
  --line:#d9d9d9;
}
*{box-sizing:border-box;margin:0;padding:0}
html,body{width:983px;height:1200px;overflow:hidden}
body{position:relative;background:var(--paper);font-family:"Source Sans 3",sans-serif;color:var(--ink)}
.abs{position:absolute}
.top-band{left:0;top:0;width:983px;height:14px;background:var(--navy)}
.header{left:0;top:14px;width:983px;height:144px;background:linear-gradient(#f7f7f7,#fdfdfd)}
.brand{left:77px;top:40px;display:flex;align-items:center;gap:10px}
.brand-mark{width:76px;height:76px;border-radius:50%;background:var(--navy)}
.brand-name{font-size:25px;font-weight:600;color:var(--red);line-height:1.05}
.brand-tag{font-size:10px;color:var(--ink);margin-top:4px;font-weight:400}
.partner{right:80px;top:30px;font-size:15px;color:#222}
.partner b{font-weight:600;margin-left:4px}
.connected{right:80px;top:73px;display:flex;align-items:center;gap:5px;font-size:11px;font-style:italic;color:#555}
.connected span{margin-right:8px}
.social{width:24px;height:24px;border-radius:50%;background:var(--navy);border:2px solid #d5d9e6}
.nav{left:359px;top:122px;display:flex;height:25px;font-size:13px;color:#444}
.nav a{display:block;padding:0 22px;line-height:25px;text-decoration:none;color:inherit;border-right:1px solid #ddd}
.nav a:last-child{border:none}
.nav a.active{background:var(--nav-red);color:#fff;padding:0 16px;margin-right:6px}
.hero{left:0;top:158px;width:983px;height:441px;background:var(--blue-band)}
.slider{left:84px;top:186px;width:813px;height:237px;background:var(--white);border-radius:8px;box-shadow:0 2px 5px rgba(0,0,0,.3)}
.slide{top:15px;height:207px}
.s1{left:18px;width:245px;background:linear-gradient(#4a86d0,#c9b09a 55%,#4f7a2e)}
.s2{left:281px;width:242px;background:linear-gradient(#5aa5e8,#cfd4d6 55%,#6f8b3f)}
.s3{left:542px;width:251px;background:linear-gradient(#7c86b8,#e5a886 35%,#5a6c7a 60%,#3f8a2a)}
.arrow{top:277px;width:24px;height:51px;background:#f6f6f6;display:flex;align-items:center;justify-content:center}
.arrow.l{left:62px;border-radius:26px 0 0 26px}
.arrow.r{left:897px;border-radius:0 26px 26px 0}
.welcome-title{left:0;top:442px;width:983px;text-align:center;font-size:25px;font-weight:300;color:#fff}
.rule{top:458px;height:1px;width:280px;border-top:1px solid rgba(255,255,255,.35)}
.welcome-text{left:87px;top:486px;width:811px;font-size:13.5px;line-height:20px;color:#fff;text-align:justify;font-weight:400}
.shade{left:80px;top:599px;width:820px;height:20px;background:radial-gradient(ellipse at top,rgba(0,0,0,.18),transparent 70%)}
.section-title{font-size:17px;font-weight:600;color:#555}
.section-title em{font-style:normal;color:var(--red)}
.upcoming-title{left:82px;top:629px}
.upcoming-rule{left:77px;top:658px;width:543px;border-top:1px solid var(--line)}
.auction{left:80px;width:542px;font-family:Arimo,sans-serif}
.auction h3{font-size:12px;font-weight:700;color:var(--red);letter-spacing:.2px;margin-bottom:9px}
.auction .row{display:flex;gap:9px}
.thumb{width:117px;height:78px;border:3px solid #ddd;background:linear-gradient(#8fb5d8,#b7a895 45%,#6ba43b);flex:none}
.info{font-size:10.5px;font-style:italic;color:#555;line-height:15px}
.info b{font-weight:700}
.info p{margin-bottom:4px}
.btns{display:flex;gap:12px;margin-top:5px}
.btn{width:55px;height:20px;border-radius:10px;color:#fff;font-size:11px;font-style:normal;display:flex;align-items:center;justify-content:center}
.btn.details{background:linear-gradient(#6c8fe0,#2f4fb0)}
.btn.photos{background:linear-gradient(#5a2a22,#1e0a08)}
.sep{left:82px;width:540px;border-top:1px solid var(--line)}
.phone-box{left:655px;top:621px;width:242px;height:40px;background:#fff;border:1px solid #e3e3e3;display:flex;align-items:center;gap:12px;padding-left:6px}
.phone-icon{width:24px;height:24px;border-radius:4px;background:#222;display:flex;align-items:center;justify-content:center}
.phone-num{font-size:24px;font-weight:300;color:var(--navy)}
.video{left:658px;top:678px;width:240px;height:155px;background:linear-gradient(#2a2a2a,#5b4c44 60%,#1a1a1a)}
.video-bar{left:0;bottom:0;width:240px;height:18px;background:#111;border-top:3px solid #c00}
.featured{left:658px;top:854px;width:240px;height:245px;background:#f6f6f6;border:1px solid #e2e2e2}
.featured .section-title{position:absolute;left:14px;top:8px}
.featured-rule{left:10px;top:34px;width:218px;border-top:1px solid var(--line)}
.featured-img{left:10px;top:43px;width:218px;height:101px;background:linear-gradient(#3f7fd0,#c3aa92 50%,#4f8a2c)}
.featured-text{left:10px;top:158px;width:218px;font-size:11.5px;line-height:15px;color:#666;text-align:justify}
.pager{left:200px;top:224px;display:flex;gap:4px}
.footer{left:0;top:1117px;width:983px;height:83px;background:var(--footer);font-family:Arimo,sans-serif;font-size:11px;color:#eee;padding:10px 0 0 87px;line-height:19px;letter-spacing:.2px}
.footer-brand{left:747px;top:1133px;display:flex;align-items:center;gap:6px;color:#bbb}
.footer-brand .dot{width:40px;height:40px;border-radius:50%;background:#666}
.footer-brand .nm{font-family:"Source Sans 3",sans-serif;font-size:13px;font-weight:600;line-height:14px}
.footer-brand small{display:block;font-size:8px;font-weight:600}
</style>
</head>
<body>
<div class="abs top-band"></div>
<header class="abs header"></header>
<div class="abs brand">
  <div class="brand-mark"></div>
  <div class="brand-name">Pellingworth<br>Auctioneers<div class="brand-tag">"The Bid You Trust!"</div></div>
</div>
<div class="abs partner">an alliance partner of<b>Meridian Alliance</b></div>
<div class="abs connected"><span>Get Connected :</span><i class="social"></i><i class="social"></i><i class="social"></i><i class="social"></i></div>
<nav class="abs nav"><a class="active">Home</a><a>Auctions</a><a>About Us</a><a>Buyers</a><a>Sellers</a><a>Contact Us</a></nav>

<section class="abs hero"></section>
<div class="abs slider">
  <div class="abs slide s1" role="img" aria-label="Photo of a stucco mansion with a curved driveway"></div>
  <div class="abs slide s2" role="img" aria-label="Photo of a country house with autumn garden"></div>
  <div class="abs slide s3" role="img" aria-label="Photo of a large shingled home at sunset"></div>
</div>
<div class="abs arrow l"><svg width="8" height="12"><path d="M7 0L0 6l7 6z" fill="#9c1f5a"/></svg></div>
<div class="abs arrow r"><svg width="8" height="12"><path d="M1 0l7 6-7 6z" fill="#9c1f5a"/></svg></div>
<div class="abs rule" style="left:93px"></div>
<div class="abs rule" style="left:613px"></div>
<h1 class="abs welcome-title">Welcome Message</h1>
<p class="abs welcome-text">Nam cursus eros tellus, in malesuada metus tempor in. Aliquam mollis at nulla quis feugiat. Aenean malesuada vulputate urna sit amet placerat. Maecenas placerat facilisis risus posuere aliquam. Aliquam erat volutpat. Vestibulum dui est, gravida vel ipsum sed, porttitor sollicitudin enim. Aliquam mattis vulputate auctor. Etiam id molestie arcu. Pellentesque ultrices cursus libero quis volutpat. Nunc porta, quam et consectetur pharetra, nisi ligula porttitor nisi, nec mollis massa libero sed sapien...</p>
<div class="abs shade"></div>

<h2 class="abs section-title upcoming-title"><em>Upcoming</em> Auctions</h2>
<div class="abs upcoming-rule"></div>

<article class="abs auction" style="top:690px">
  <h3>Incredible Home in Brook Hollow' exclusive Cedar Ridge community</h3>
  <div class="row"><div class="thumb" role="img" aria-label="Photo of the auction property"></div>
  <div class="info"><p><b>Begins:</b>&nbsp; Tuesday, April 23, 2013 at 10:00 AM EDT</p><p><b>Location:</b>&nbsp; Cedar Ridge Entrance- 1450 N. Orchard Hwy 9 &nbsp;Cedar Ridge Rd (Auction Property) &nbsp; Brook Hollow, FL 33999</p>
  <div class="btns"><span class="btn details">Details</span><span class="btn photos">Photos</span></div></div></div>
</article>
<div class="abs sep" style="top:803px"></div>
<article class="abs auction" style="top:822px">
  <h3>Incredible Home in Brook Hollow' exclusive Cedar Ridge community</h3>
  <div class="row"><div class="thumb" role="img" aria-label="Photo of the auction property"></div>
  <div class="info"><p><b>Begins:</b>&nbsp; Tuesday, April 23, 2013 at 10:00 AM EDT</p><p><b>Location:</b>&nbsp; Cedar Ridge Entrance- 1450 N. Orchard Hwy 9 &nbsp;Cedar Ridge Rd (Auction Property) &nbsp; Brook Hollow, FL 33999 Lorem Ipsum has been the industry's standard dummy text ever since the 1500s,</p>
  <div class="btns"><span class="btn details">Details</span><span class="btn photos">Photos</span></div></div></div>
</article>
<div class="abs sep" style="top:950px"></div>
<article class="abs auction" style="top:966px">
  <h3>Incredible Home in Brook Hollow' exclusive Cedar Ridge community</h3>
  <div class="row"><div class="thumb" role="img" aria-label="Photo of the auction property"></div>
  <div class="info"><p><b>Begins:</b>&nbsp; Tuesday, April 23, 2013 at 10:00 AM EDT</p><p><b>Location:</b>&nbsp; Cedar Ridge Entrance- 1450 N. Orchard Hwy 9 &nbsp;Cedar Ridge Rd (Auction Property) &nbsp; Brook Hollow, FL 33999 Lorem Ipsum has been the industry's standard dummy text ever since the 1500s,</p>
  <div class="btns"><span class="btn details">Details</span><span class="btn photos">Photos</span></div></div></div>
</article>

<aside>
  <div class="abs phone-box"><span class="phone-icon"><svg width="12" height="14" viewBox="0 0 12 14"><path d="M3 1c-2 1-2 3-1 6s3 5 5 6c1 0 2-1 2-2l-2-2-1 1C5 9 4 7 4 6l1-1-1-3z" fill="#fff"/></svg></span><span class="phone-num">(012) 555 014 2900</span></div>
  <div class="abs video" role="img" aria-label="Video player showing a company video">
    <svg class="abs" style="left:102px;top:55px" width="36" height="28"><rect width="36" height="28" rx="6" fill="rgba(0,0,0,.6)"/><path d="M14 8l10 6-10 6z" fill="#fff"/></svg>
    <div class="abs video-bar"></div>
  </div>
  <div class="abs featured">
    <h2 class="section-title"><em>Featured</em> Auction</h2>
    <div class="abs featured-rule"></div>
    <div class="abs featured-img" role="img" aria-label="Photo of the featured mansion"></div>
    <p class="abs featured-text">Morbi mollis nibh nulla, et eleifend arcu aliquet id. Nullam eu massa leo. Proin turpis metus, tempor ac auctor quis, iaculis sit amet sem...</p>
    <div class="abs pager"><svg width="7" height="10"><path d="M6 1L2 5l4 4" stroke="#aaa" stroke-width="2" fill="none"/></svg><svg width="7" height="10"><path d="M1 1l4 4-4 4" stroke="#333" stroke-width="2" fill="none"/></svg></div>
  </div>
</aside>

<footer class="abs footer">
  Harwick and Company Auctioneers<br>
  418 Elm Avenue NW • Fairview, FL 33001<br>
  P: 555-014-2867 • F: 555-014-2869 • info@HarwickAuctioneers.com<br>
  Copyright © 2008 - 2013 • Harwick and Company Auctioneers • All Rights Reserved.
</footer>
<div class="abs footer-brand"><span class="dot"></span><span class="nm">Pellingworth<br>Auctioneers<small>an alliance partner of Meridian Alliance</small></span></div>
</body>
</html>
```